TRELBY Construction Group business card for distribution

A business card detailing our services, with our phone number and email address.
- Groundworks / Foundations / Drainage
- Landscaping / Hard Landscaping / Patios / Decking
- Fencing
The card should include company logo and be in the same colours.

Target Market(s)
Domestic Houses
Industry/Entity Type
Construction
Contact Information for Business Card
Phone Number - 07731 248 905 / 07612093184. Email address: trelbygroup@fenwickmail.com
Font styles to use
Serif
Sans Serif
Colors
F0912C
F2A743
F7CA91
FBE8D2
FDF5EE
Requirements
Must have
- Contact numbers. Photos of past work. Company Logo

Nice to have
- Company Logo

```html
<!DOCTYPE html>
<html lang="en">
<head>
<meta charset="utf-8">
<title>TRELBY Construction Group – Business Card</title>
<link rel="stylesheet" href="https://fonts.googleapis.com/css2?family=Montserrat:wght@700&family=Roboto:wght@400;500;700&display=swap">
<style>
  :root {
    --page: #151515;
    --card: #2a2a2a;
    --card-edge: #f0912c;
    --orange: #f0912c;
    --amber: #f2a743;
    --white: #ffffff;
    --muted: #d9d9d9;
    --emboss: #3b3b3b;
  }
  * { box-sizing: border-box; margin: 0; padding: 0; }
  html, body { width: 1200px; height: 840px; overflow: hidden; background: var(--page); }
  .canvas {
    width: 1200px; height: 840px;
    display: flex; flex-direction: column; align-items: center; justify-content: center; gap: 34px;
  }
  .card {
    position: relative;
    width: 620px; height: 354px;
    background: linear-gradient(160deg, #2f2f2f 0%, var(--card) 55%, #262626 100%);
    border-radius: 24px;
    box-shadow: 0 5px 0 var(--card-edge), 0 18px 30px rgba(0,0,0,.55);
    overflow: hidden;
    font-family: "Roboto", Arial, sans-serif;
    color: var(--white);
  }

  /* Services side */
  .card--services { display: flex; flex-direction: column; align-items: center; }
  .brand--emboss {
    margin-top: 58px;
    display: flex; align-items: center; gap: 14px;
  }
  .brand-mark { width: 26px; height: 26px; background: var(--orange); }
  .brand--emboss .brand-mark { background: var(--emboss); }
  .brand-name {
    font-family: "Montserrat", Arial, sans-serif; font-weight: 700;
    line-height: 1.05; letter-spacing: 2px;
  }
  .brand--emboss .brand-name { color: var(--emboss); }
  .brand-name .big { display: block; font-size: 52px; letter-spacing: 4px; }
  .brand-name .small { display: block; font-size: 15px; letter-spacing: 3.5px; }

  .services-band {
    margin-top: 30px;
    width: 420px; height: 34px;
    background: linear-gradient(90deg, rgba(240,145,44,0) 0%, var(--orange) 30%, var(--amber) 70%, rgba(242,167,67,0) 100%);
    display: flex; align-items: center; justify-content: center;
    font-weight: 700; font-size: 17px; letter-spacing: .5px;
  }
  .services-list {
    list-style: none; margin-top: 16px; text-align: center;
    font-size: 17px; line-height: 1.5;
  }
  .services-list li::before {
    content: ""; display: inline-block; width: 7px; height: 7px; border-radius: 50%;
    background: var(--orange); margin-right: 6px; vertical-align: middle;
  }

  /* Contact side */
  .card--contact { display: flex; align-items: center; padding: 0 40px 0 46px; }
  .brand--contact { display: flex; align-items: center; gap: 12px; width: 262px; }
  .brand--contact .brand-name { color: var(--white); }
  .brand--contact .big { font-size: 40px; letter-spacing: 3px; }
  .brand--contact .small { font-size: 11.5px; letter-spacing: 2.4px; }
  .divider { width: 1.5px; height: 150px; background: var(--muted); margin: 0 24px; }
  .contact-details { display: flex; flex-direction: column; }
  .person-name { color: var(--orange); font-weight: 700; font-size: 24px; letter-spacing: .3px; }
  .person-role { font-size: 17px; margin-bottom: 12px; }
  .contact-line { display: flex; align-items: center; gap: 8px; font-size: 16px; line-height: 1.6; }
  .contact-line svg { width: 16px; height: 16px; flex: none; fill: var(--orange); }
</style>
</head>
<body>
<main class="canvas">

  <section class="card card--services" aria-label="Services side">
    <div class="brand brand--emboss">
      <span class="brand-mark"></span>
      <p class="brand-name"><span class="big">TRELBY</span><span class="small">CONSTRUCTION GROUP LTD</span></p>
    </div>
    <div class="services-band">OUR SERVICES</div>
    <ul class="services-list">
      <li>Groundworks / Foundations / Drainage</li>
      <li>Landscaping / Hard Landscaping / Patios / Decking</li>
      <li>Fencing</li>
    </ul>
  </section>

  <section class="card card--contact" aria-label="Contact side">
    <div class="brand brand--contact">
      <span class="brand-mark"></span>
      <p class="brand-name"><span class="big">TRELBY</span><span class="small">CONSTRUCTION GROUP LTD</span></p>
    </div>
    <div class="divider"></div>
    <div class="contact-details">
      <p class="person-name">MARCUS HALE</p>
      <p class="person-role">Manager</p>
      <p class="contact-line">
        <svg viewBox="0 0 24 24" aria-hidden="true"><path d="M6.6 10.8a15.1 15.1 0 0 0 6.6 6.6l2.2-2.2a1 1 0 0 1 1-.25 11.4 11.4 0 0 0 3.6.57 1 1 0 0 1 1 1V20a1 1 0 0 1-1 1A17 17 0 0 1 3 4a1 1 0 0 1 1-1h3.5a1 1 0 0 1 1 1c0 1.25.2 2.45.57 3.57a1 1 0 0 1-.25 1z"/></svg>
        07731 248 905
      </p>
      <p class="contact-line">
        <svg viewBox="0 0 24 24" aria-hidden="true"><path d="M6.6 10.8a15.1 15.1 0 0 0 6.6 6.6l2.2-2.2a1 1 0 0 1 1-.25 11.4 11.4 0 0 0 3.6.57 1 1 0 0 1 1 1V20a1 1 0 0 1-1 1A17 17 0 0 1 3 4a1 1 0 0 1 1-1h3.5a1 1 0 0 1 1 1c0 1.25.2 2.45.57 3.57a1 1 0 0 1-.25 1z"/></svg>
        07612093184
      </p>
      <p class="contact-line">
        <svg viewBox="0 0 24 24" aria-hidden="true"><path d="M3 5h18a1 1 0 0 1 1 1v12a1 1 0 0 1-1 1H3a1 1 0 0 1-1-1V6a1 1 0 0 1 1-1zm1 2.4V17h16V7.4l-8 5.3z M4.6 7 12 11.9 19.4 7z"/></svg>
        trelbygroup@fenwickmail.com
      </p>
    </div>
  </section>

</main>
</body>
</html>
```